Bracken Project Services - Flyer

I need a single page A4 Capability Statement, which will be used to market our services to prospective clients, both in print and via email PDF.
It needs to look professional and should incorporate the elements I have uploaded into files, these include:
Capability Statement Text
Bracken Services Company Logo
Additional Logo’s (Tools We Use)
Frame Cellar Pics can be cut into the page
I have included examples of capability statements as a guide to what i am looking for.
Regards
Derek
Engineering Consulting

```html
<!DOCTYPE html>
<html lang="en">
<head>
<meta charset="utf-8">
<title>Bracken Project Services – Capability Statement</title>
<link href="https://fonts.googleapis.com/css2?family=Arimo:wght@400;700&display=swap" rel="stylesheet">
<style>
  :root {
    --brand-blue: #4a86c5;
    --deep-blue: #3f78c0;
    --title-blue: #4f8fcf;
    --sky: #92d0ec;
    --bullet: #5aa6d8;
    --ink: #222;
    --body-blue: #3a6fb5;
    --grey-top: #e9ecef;
    --grey-bottom: #c9cbcd;
    --white: #fff;
  }
  * { margin: 0; padding: 0; box-sizing: border-box; }
  html, body { width: 848px; height: 1200px; overflow: hidden; }
  body { font-family: "Arimo", Arial, sans-serif; color: var(--ink); background: var(--white); }

  .flyer {
    position: relative; width: 848px; height: 1200px; overflow: hidden;
    background: linear-gradient(180deg, var(--grey-top) 0%, #e2e4e6 50%, var(--grey-bottom) 100%);
  }

  .header-backdrop {
    position: absolute; left: 0; top: 0; width: 848px; height: 160px;
    background: linear-gradient(90deg, #f3f4f6, #e5e8eb);
  }
  .accent-band {
    position: absolute; left: 0; top: 150px; width: 848px; height: 12px;
    background: var(--sky);
  }
  .header-card {
    position: absolute; left: 0; top: 0; width: 548px; height: 143px;
    background: var(--white); border-bottom-right-radius: 40px;
    box-shadow: 2px 3px 6px rgba(0,0,0,.12);
  }
  .doc-title {
    position: absolute; left: 92px; top: 30px;
    font-size: 29px; font-weight: 400; line-height: 1.3; color: var(--title-blue);
  }

  .brand {
    position: absolute; left: 584px; top: 36px; width: 200px; text-align: center;
  }
  .brand-dot {
    width: 54px; height: 54px; border-radius: 50%; margin: 0 auto 12px;
    background: var(--brand-blue);
  }
  .brand-name {
    font-size: 14px; font-weight: 700; letter-spacing: .5px; color: #333; line-height: 1.2;
  }

  .hero-photo {
    position: absolute; left: 0; top: 162px; width: 848px; height: 260px;
    background: linear-gradient(120deg, #dfe6ee 0%, #c9d6e4 35%, #eef2f6 60%, #b9c7d6 100%);
    clip-path: polygon(0 0, 100% 0, 100% 100%, 30% 100%, 0 55%);
  }

  .about-tab {
    position: absolute; left: 395px; top: 373px; width: 453px; height: 58px;
    background: var(--deep-blue); border-radius: 22px 0 0 22px;
    color: var(--white); font-size: 38px; line-height: 58px; letter-spacing: 1.5px;
    padding-left: 139px;
  }

  .services-card {
    position: absolute; left: 28px; top: 403px; width: 407px; height: 590px;
    background: var(--white); border-top-right-radius: 57px;
    padding: 10px 0 0 29px;
  }
  .services-heading { font-size: 26px; line-height: 30px; color: var(--body-blue); font-weight: 400; }
  .service-group-title { font-size: 23px; line-height: 30px; color: var(--body-blue); font-weight: 400; margin: 6px 0 8px; }
  .services-heading + .service-group-title { margin-top: 15px; margin-bottom: 5px; }
  .service-list { list-style: none; }
  .service-list li {
    position: relative; padding-left: 32px; font-size: 14px; color: var(--body-blue);
    line-height: 23.3px; white-space: nowrap;
  }
  .service-list li::before {
    content: ""; position: absolute; left: 4px; top: 6px;
    width: 11px; height: 11px; border-radius: 50%; background: var(--bullet);
  }

  .contact-box {
    position: absolute; left: 28px; top: 1015px; width: 364px; height: 161px;
    background: var(--sky); border-top-left-radius: 30px;
    padding: 12px 39px 0 0; text-align: right; font-size: 16.5px; line-height: 26px;
    color: var(--ink); font-style: normal;
  }

  .about-card {
    position: absolute; left: 425px; top: 463px; width: 390px; height: 713px;
    background: var(--white); border-radius: 26px;
  }
  .about-copy {
    position: absolute; left: 22px; top: 39px; width: 341px;
    padding: 2px 10px 2px 0; border-right: 4px solid var(--deep-blue);
    text-align: right; font-size: 13.5px; line-height: 19px; color: var(--body-blue);
  }
  .about-copy p + p { margin-top: 19px; }

  .tools-heading {
    position: absolute; left: 40px; top: 434px; font-size: 17px; font-weight: 400;
    line-height: 20px; color: var(--ink); letter-spacing: .4px;
  }
  .tool-grid {
    position: absolute; left: 38px; top: 469px; width: 330px;
    display: grid; grid-template-columns: 200px 130px; grid-auto-rows: 36px; row-gap: 25px;
  }
  .tool {
    display: flex; align-items: center; gap: 8px; white-space: nowrap;
    font-size: 15px; font-weight: 700; color: #555;
  }
  .tool-mark { width: 14px; height: 14px; background: var(--brand-blue); flex: none; }
</style>
</head>
<body>
<main class="flyer">
  <div class="header-backdrop"></div>
  <div class="accent-band"></div>
  <div class="hero-photo" role="img" aria-label="Photo of a project schedule printout with hands holding a pen at a desk"></div>

  <header class="header-card">
    <h1 class="doc-title">Capability Statement<br>Services Programme</h1>
  </header>
  <div class="brand">
    <div class="brand-dot"></div>
    <div class="brand-name">BRACKEN PROJECT<br>SERVICES</div>
  </div>

  <div class="about-tab">About Us:</div>

  <section class="services-card">
    <h2 class="services-heading">CORE SERVICES:</h2>
    <h3 class="service-group-title">Planning and Scheduling</h3>
    <ul class="service-list">
      <li>Tender Planning</li>
      <li>Interactive Planning / Pull Planning</li>
      <li>EPCMV Planning &amp; Scheduling</li>
      <li>Schedule Earned Value Management</li>
      <li>Independent Schedule Quality Assessment</li>
      <li>Schedule Risk Analysis (Monte Carlo)</li>
      <li>Training</li>
    </ul>
    <h3 class="service-group-title">Management of Risk</h3>
    <ul class="service-list">
      <li>Risk Management Policies &amp; Procedures</li>
      <li>Risk Management Strategy</li>
      <li>Risk Registers</li>
      <li>Risk Improvement Planning</li>
      <li>Risk Response and Communication</li>
      <li>Risk Management Training</li>
    </ul>
    <h3 class="service-group-title">Management of Risk</h3>
    <ul class="service-list">
      <li>Estimating &amp; Forecasting</li>
      <li>Earned Value Analysis</li>
      <li>Progress Reporting</li>
      <li>Cost Risk Analysis</li>
    </ul>
  </section>

  <address class="contact-box">
    Contact:<br>
    Derek Hallam (Managing Director)<br>
    info@brackenservices.ie<br>
    www.brackenservices.ie<br>
    +353 (0)870 555 014
  </address>

  <section class="about-card">
    <div class="about-copy">
      <p>Bracken Project Services Ltd. is a leading project control consultancy based in Co Clare Ireland</p>
      <p>For over 20 years we have been helping our clients to deliver complex projects and programs throughout mainland Europe.</p>
      <p>We are passionate about empower organisations to achieve their objectives, on time and on budget.</p>
      <p>We are continually innovating, evolving and learning, utilize the latest industry tools and techniques to deliver real value to our clients.</p>
      <p>Our goal is to make successful project delivery more achievable and repeatable.</p>
    </div>
    <h3 class="tools-heading">BRACKEN SERVICES COMPANY:</h3>
    <div class="tool-grid">
      <div class="tool"><span class="tool-mark"></span>Keystone Planner</div>
      <div class="tool"><span class="tool-mark"></span>Tasklane</div>
      <div class="tool"><span class="tool-mark"></span>Riskwell</div>
      <div class="tool"><span class="tool-mark"></span>Markpoint Pro</div>
      <div class="tool"><span class="tool-mark"></span>Gridline Scheduler</div>
      <div class="tool"></div>
      <div class="tool"><span class="tool-mark"></span>Northvale Gauge</div>
    </div>
  </section>
</main>
</body>
</html>
```